Pages That Sell Services - book cover (front panel only)

I want a book cover (for print and ebook) in a distinctive, quirky style that can be repurposed for podcast artwork too. Full brief supplied.
The book is a practical, accessible handbook for anyone thinking about writing a book to build their business, with a wide range of tips and techniques to help plan, write, publishing and promote a book that’s integrated with your platform and works to build your reputation, network and credibility from day 1.
The target audience is experts in business, particularly owners of SMEs with an established online and offline platform (eg speaking, training, consulting) who want to add a book to take their business to the next level.
I want the design to be strong and distinctive, slightly quirky without being gimmicky, with the focus on typography.

Target Market(s)

Those writing a book based on their expertise to build their business

Industry/Entity Type

Publishing Company

Font styles to use
Serif
Sans Serif
Decorative

Colors

Designer to choose colors to be used in the design.

Requirements
Must have
• Commercially appealing book cover design, with application files and copyright supplied, front panel only, 5.5 x 8.5 inch format. Must work at both full size and thumbnail.
Nice to have
• A distinctive style that could be applied across other products in my portfolio.

```html
<!DOCTYPE html>
<html lang="en">
<head>
<meta charset="utf-8">
<title>Pages That Sell Services – Book Cover</title>
<link rel="stylesheet" href="https://fonts.googleapis.com/css2?family=Oswald:wght@500;700&family=Roboto+Condensed:wght@300;400&display=swap">
<style>
  :root {
    --backdrop: #dcbfa6;
    --cover: #f2f2f1;
    --ink-title-dark: #2f3a12;
    --ink-title-mid: #6f7d22;
    --ink-title-light: #b9a640;
    --ink-subtitle: #2a2a2a;
    --cloud-faint: #dadada;
    --cloud-light: #c8c8c8;
    --cloud-mid: #adadad;
    --cloud-strong: #8e8e8e;
    --cloud-dark: #6a6a6a;
    --author: #5a6a1a;
  }
  html, body {
    margin: 0;
    width: 1200px;
    height: 960px;
    overflow: hidden;
    background: var(--backdrop);
  }
  .stage {
    position: relative;
    width: 1200px;
    height: 960px;
  }
  .book-cover {
    position: absolute;
    left: 309px;
    top: 30px;
    width: 582px;
    height: 900px;
    background: var(--cover);
  }
  .book-cover svg { display: block; }
  .title-line {
    font-family: "Oswald", "Arial Narrow", sans-serif;
    font-weight: 700;
    text-transform: uppercase;
  }
  .subtitle {
    font-family: "Oswald", "Arial Narrow", sans-serif;
    font-weight: 500;
    font-size: 15px;
    fill: var(--ink-subtitle);
    letter-spacing: 0.4px;
  }
  .cloud-word {
    font-family: "Roboto Condensed", "Arial Narrow", sans-serif;
    font-weight: 400;
    text-transform: uppercase;
  }
  .tone-faint { fill: var(--cloud-faint); }
  .tone-light { fill: var(--cloud-light); }
  .tone-mid { fill: var(--cloud-mid); }
  .tone-strong { fill: var(--cloud-strong); }
  .tone-dark { fill: var(--cloud-dark); }
  .author-name {
    font-family: "Oswald", "Arial Narrow", sans-serif;
    font-weight: 700;
    font-size: 19px;
    fill: var(--author);
    letter-spacing: 0.5px;
  }
</style>
</head>
<body>
<div class="stage">
  <div class="book-cover">
    <svg width="582" height="900" viewBox="0 0 582 900" xmlns="http://www.w3.org/2000/svg">
      <defs>
        <linearGradient id="title-meadow" x1="0" y1="0" x2="1" y2="1">
          <stop offset="0" stop-color="var(--ink-title-light)"/>
          <stop offset="0.45" stop-color="var(--ink-title-mid)"/>
          <stop offset="1" stop-color="var(--ink-title-dark)"/>
        </linearGradient>
      </defs>

      <g class="title-block" fill="url(#title-meadow)" role="img" aria-label="Title lettering filled with a green and golden meadow texture">
        <text class="title-line" x="291" y="168" font-size="40" text-anchor="middle" textLength="210" lengthAdjust="spacingAndGlyphs">Pages That</text>
        <text class="title-line" x="291" y="228" font-size="62" text-anchor="middle" textLength="150" lengthAdjust="spacingAndGlyphs">Sell</text>
        <text class="title-line" x="291" y="306" font-size="88" text-anchor="middle" textLength="400" lengthAdjust="spacingAndGlyphs">Services</text>
      </g>

      <g class="subtitle-block">
        <text class="subtitle" x="291" y="332" text-anchor="middle" textLength="400" lengthAdjust="spacingAndGlyphs">SMART STEPS TO SHAPE AND SHIP A BOOK THAT</text>
        <text class="subtitle" x="291" y="351" text-anchor="middle" textLength="290" lengthAdjust="spacingAndGlyphs">WINS CLIENTS FOR YOUR EXPERTISE</text>
      </g>

      <g class="word-cloud">
        <text class="cloud-word tone-light" x="70" y="440" font-size="30" textLength="90" lengthAdjust="spacingAndGlyphs">Reach</text>
        <text class="cloud-word tone-mid" x="170" y="440" font-size="12" textLength="58" lengthAdjust="spacingAndGlyphs">Chapter</text>
        <text class="cloud-word tone-strong" x="238" y="440" font-size="36" textLength="170" lengthAdjust="spacingAndGlyphs">Authority</text>
        <text class="cloud-word tone-light" x="418" y="440" font-size="18" textLength="50" lengthAdjust="spacingAndGlyphs">Pitch</text>

        <text class="cloud-word tone-faint" x="60" y="480" font-size="48" textLength="200" lengthAdjust="spacingAndGlyphs">Expertise</text>
        <text class="cloud-word tone-mid" x="270" y="480" font-size="20" textLength="80" lengthAdjust="spacingAndGlyphs">Outline</text>
        <text class="cloud-word tone-mid" x="358" y="480" font-size="30" textLength="70" lengthAdjust="spacingAndGlyphs">Voice</text>
        <text class="cloud-word tone-light" x="436" y="480" font-size="16" textLength="46" lengthAdjust="spacingAndGlyphs">Draft</text>

        <text class="cloud-word tone-light" x="60" y="506" font-size="16" textLength="80" lengthAdjust="spacingAndGlyphs">Speaking</text>
        <text class="cloud-word tone-light" x="148" y="506" font-size="16" textLength="80" lengthAdjust="spacingAndGlyphs">Training</text>
        <text class="cloud-word tone-strong" x="270" y="506" font-size="22" textLength="90" lengthAdjust="spacingAndGlyphs">Clients</text>
        <text class="cloud-word tone-mid" x="368" y="506" font-size="22" textLength="46" lengthAdjust="spacingAndGlyphs">Edit</text>
        <text class="cloud-word tone-light" x="420" y="506" font-size="22" textLength="60" lengthAdjust="spacingAndGlyphs">Story</text>

        <text class="cloud-word tone-faint" x="522" y="420" font-size="18" text-anchor="middle">T</text>
        <text class="cloud-word tone-faint" x="522" y="442" font-size="18" text-anchor="middle">R</text>
        <text class="cloud-word tone-faint" x="522" y="464" font-size="18" text-anchor="middle">U</text>
        <text class="cloud-word tone-faint" x="522" y="486" font-size="18" text-anchor="middle">S</text>
        <text class="cloud-word tone-faint" x="522" y="508" font-size="18" text-anchor="middle">T</text>

        <text class="cloud-word tone-light" x="60" y="580" font-size="74" textLength="330" lengthAdjust="spacingAndGlyphs">Credibility</text>
        <text class="cloud-word tone-dark" x="400" y="558" font-size="38" textLength="120" lengthAdjust="spacingAndGlyphs">Launch</text>
        <text class="cloud-word tone-light" x="402" y="580" font-size="16" textLength="70" lengthAdjust="spacingAndGlyphs">Podcast</text>
        <text class="cloud-word tone-mid" x="480" y="582" font-size="22" textLength="60" lengthAdjust="spacingAndGlyphs">Value</text>

        <text class="cloud-word tone-dark" x="60" y="630" font-size="40" textLength="120" lengthAdjust="spacingAndGlyphs">Publish</text>
        <text class="cloud-word tone-strong" x="190" y="630" font-size="28" textLength="110" lengthAdjust="spacingAndGlyphs">Readers</text>
        <text class="cloud-word tone-light" x="310" y="630" font-size="20" textLength="110" lengthAdjust="spacingAndGlyphs">Consulting</text>

        <text class="cloud-word tone-faint" x="522" y="612" font-size="18" text-anchor="middle">G</text>
        <text class="cloud-word tone-faint" x="522" y="634" font-size="18" text-anchor="middle">R</text>
        <text class="cloud-word tone-faint" x="522" y="656" font-size="18" text-anchor="middle">O</text>
        <text class="cloud-word tone-faint" x="522" y="678" font-size="18" text-anchor="middle">W</text>

        <text class="cloud-word tone-light" x="60" y="670" font-size="30" textLength="130" lengthAdjust="spacingAndGlyphs">Audience</text>
        <text class="cloud-word tone-mid" x="198" y="670" font-size="10" textLength="52" lengthAdjust="spacingAndGlyphs">Network</text>
        <text class="cloud-word tone-strong" x="260" y="670" font-size="36" textLength="210" lengthAdjust="spacingAndGlyphs">Reputation</text>

        <text class="cloud-word tone-dark" x="140" y="712" font-size="34" textLength="90" lengthAdjust="spacingAndGlyphs">Share</text>
        <text class="cloud-word tone-light" x="240" y="712" font-size="14" textLength="40" lengthAdjust="spacingAndGlyphs">Plan</text>
        <text class="cloud-word tone-light" x="290" y="712" font-size="24" textLength="120" lengthAdjust="spacingAndGlyphs">Momentum</text>

        <text class="cloud-word tone-faint" x="90" y="750" font-size="24" textLength="130" lengthAdjust="spacingAndGlyphs">Signature</text>
        <text class="cloud-word tone-strong" x="230" y="750" font-size="30" textLength="110" lengthAdjust="spacingAndGlyphs">System</text>
      </g>

      <text class="author-name" x="395" y="818">MAREN HOLT</text>
    </svg>
  </div>
</div>
</body>
</html>
```